Ridgeway Moss - Facebook Cover Photo & Photo Icon Design

We’re looking for a Facebook Cover Photo and Profile Icon design for Ridgeway Moss, a leading Residential Real Estate brand under Ridgeway Property Agents, based in Capalaba and Alexandra Hills, Queensland, Australia.

This design will represent my professional real estate profile and needs to be bold, clean, and on-brand.

Deliverables:

Facebook Cover Photo (820 x 312 px, optimized for mobile + desktop)

Facebook Profile Icon (1:1 ratio, minimum 320 x 320 px)

Design Guidelines:

1. Must Include:

The Ridgeway Moss logo (provided after project start)

Use of the Ridgeway Property Agents brand colour palette (will be supplied)

Clear connection to residential real estate

2. Optional but Preferred:

A local photo or skyline of Capalaba or Alexandra Hills in QLD (bonus points for this)

Space for a short tagline like:
“Selling Faster. Selling Smarter. Selling Ridgeway.”
(Optional tagline – open to variations if it improves layout/design)

3. Style & Feel:

Professional yet personable

Clean, modern aesthetic

Subtle touches of fun or personality are welcome

Layout must work well when overlaid by Facebook UI elements (like profile photo & call-to-action buttons)

Who I Am:
I'm a well-known residential real estate agent in the Redlands area, known for high-energy campaigns, premium video marketing, and a results-driven approach. My brand is fun, fresh, and high-performing — just like the real estate campaigns I run.

Files to be Provided (after selection):

Ridgeway Moss logo in high-res

Brand colour palette / style reference

Optional photo references if local imagery is not sourced by designer

Final Notes:

Make sure all text is legible on mobile and desktop

Original, layered design files must be delivered (PSD or AI preferred)

Bonus points if it feels uniquely “Bayside Queensland” while maintaining a national-level professional polish

Target Market(s)

Alexandra Hills, Capalaba & Sheldon

Industry/Entity Type

Real Estate

Colors
0054AA
0677BA
7BADD7
CADEEF
E8F1F8

Requirements
Must have
• Headshot, Mobile Number 0491 726 805, Suburbs - Alexandra Hills, Capalaba & Sheldon
Nice to have
• White, Crisp & Professional. Bottom Banner with Suburb List. Specialising in Alexandra Hills, Capalaba & Sheldon

```html
<!DOCTYPE html>
<html lang="en">
<head>
<meta charset="utf-8">
<title>Ridgeway Moss – Facebook Cover &amp; Profile Icon</title>
<link href="https://fonts.googleapis.com/css2?family=Play:wght@400;700&display=swap" rel="stylesheet">
<style>
  :root {
    --navy: #0d1f5c;
    --tan: #d4a467;
    --ink: #111318;
    --sky-top: #eef4f9;
    --sky-mid: #dde8f1;
    --sky-low: #cfdde9;
    --photo-sky: #dfe3e8;
    --photo-house: #a9aeb4;
    --photo-lawn: #4f8a33;
    --stage: #ececec;
    --paper: #ffffff;
  }
  * { box-sizing: border-box; margin: 0; padding: 0; }
  html, body { width: 1200px; height: 447px; overflow: hidden; }
  body {
    background: var(--stage);
    font-family: "Play", sans-serif;
    position: relative;
  }

  .cover, .profile-icon {
    position: absolute;
    overflow: hidden;
    background: var(--paper);
  }
  .cover { left: 20px; top: 67px; width: 820px; height: 312px; }
  .profile-icon { left: 860px; top: 63px; width: 320px; height: 320px; }

  .skyline-backdrop {
    position: absolute; inset: 0;
    background: linear-gradient(180deg, var(--sky-top) 0%, var(--sky-mid) 55%, var(--sky-low) 100%);
    opacity: 0.75;
  }
  .cover .skyline-backdrop { right: auto; width: 420px; }

  .brand-name {
    position: absolute;
    color: var(--navy);
    font-weight: 400;
    font-size: 28px;
    letter-spacing: 3px;
    line-height: 1;
    text-transform: uppercase;
    white-space: nowrap;
  }
  .cover .brand-name { left: 18px; top: 58px; max-width: 290px; }
  .profile-icon .brand-name { left: 0; right: 0; top: 54px; text-align: center; font-size: 28px; }

  .tagline {
    position: absolute;
    list-style: none;
    font-weight: 700;
    font-size: 23px;
    line-height: 35px;
    white-space: nowrap;
  }
  .cover .tagline { left: 18px; top: 124px; }
  .profile-icon .tagline { left: 0; right: 0; top: 125px; text-align: center; font-size: 24px; line-height: 38px; }
  .tagline .lead { color: var(--tan); }
  .tagline .key { color: var(--navy); }

  .phone {
    position: absolute;
    display: flex; align-items: center; gap: 12px;
    color: var(--ink);
    font-weight: 700;
    font-size: 34px;
    letter-spacing: 1px;
    white-space: nowrap;
  }
  .cover .phone { left: 18px; top: 258px; }
  .profile-icon .phone { left: 8px; top: 268px; font-size: 32px; gap: 10px; }
  .phone-icon { width: 34px; height: 34px; flex: none; }

  .cover-art { position: absolute; inset: 0; width: 820px; height: 312px; }
</style>
</head>
<body>

<section class="cover" aria-label="Facebook cover photo">
  <div class="skyline-backdrop" role="img" aria-label="Faint aerial view of a bayside city skyline"></div>

  <svg class="cover-art" viewBox="0 0 820 312">
    <defs>
      <linearGradient id="house-photo-tone" x1="0" y1="0" x2="0" y2="1">
        <stop offset="0" stop-color="var(--photo-sky)"/>
        <stop offset="0.45" stop-color="var(--photo-house)"/>
        <stop offset="0.68" stop-color="#6f7a6a"/>
        <stop offset="0.78" stop-color="var(--photo-lawn)"/>
        <stop offset="1" stop-color="#3f7428"/>
      </linearGradient>
    </defs>
    <path role="img" aria-label="Photo of a modern family home with palm trees and a green front lawn"
          d="M402,0 C332,92 338,232 478,312 L820,312 L820,0 Z" fill="url(#house-photo-tone)"/>
    <path class="swoosh-navy" d="M372,0 L402,0 C332,92 338,232 478,312 L408,312 C318,244 306,92 372,0 Z" fill="var(--navy)"/>
    <path class="swoosh-tan" d="M352,0 L364,0 C298,92 306,238 398,312 L382,312 C286,240 284,92 352,0 Z" fill="var(--tan)"/>
  </svg>

  <p class="brand-name">Ridgeway Moss</p>

  <ul class="tagline">
    <li><span class="lead">Selling</span> <span class="key">Faster.</span></li>
    <li><span class="lead">Selling</span> <span class="key">Smarter.</span></li>
    <li><span class="lead">Selling</span> <span class="key">Ridgeway.</span></li>
  </ul>

  <p class="phone">
    <svg class="phone-icon" viewBox="0 0 24 24" fill="none" stroke="var(--navy)" stroke-width="1.4" stroke-linejoin="round" aria-hidden="true">
      <path d="M5 3.5l3 0 1.5 4-2 1.5c1 2.3 2.8 4.1 5 5l1.5-2 4 1.5 0 3c0 1-.8 1.8-1.8 1.8C9.7 18.3 3.2 11.8 3.2 5.3 3.2 4.3 4 3.5 5 3.5z"/>
      <path d="M14 3.5a6.5 6.5 0 0 1 6.5 6.5M14 6.5a3.5 3.5 0 0 1 3.5 3.5"/>
    </svg>
    <span>0491 726 805</span>
  </p>
</section>

<section class="profile-icon" aria-label="Facebook profile icon">
  <div class="skyline-backdrop" role="img" aria-label="Faint aerial view of a bayside city skyline"></div>

  <p class="brand-name">Ridgeway Moss</p>

  <ul class="tagline">
    <li><span class="lead">Selling</span> <span class="key">Faster.</span></li>
    <li><span class="lead">Selling</span> <span class="key">Smarter.</span></li>
    <li><span class="lead">Selling</span> <span class="key">Ridgeway.</span></li>
  </ul>

  <p class="phone">
    <svg class="phone-icon" viewBox="0 0 24 24" fill="none" stroke="var(--navy)" stroke-width="1.4" stroke-linejoin="round" aria-hidden="true">
      <path d="M5 3.5l3 0 1.5 4-2 1.5c1 2.3 2.8 4.1 5 5l1.5-2 4 1.5 0 3c0 1-.8 1.8-1.8 1.8C9.7 18.3 3.2 11.8 3.2 5.3 3.2 4.3 4 3.5 5 3.5z"/>
      <path d="M14 3.5a6.5 6.5 0 0 1 6.5 6.5M14 6.5a3.5 3.5 0 0 1 3.5 3.5"/>
    </svg>
    <span>0491 726 805</span>
  </p>
</section>

</body>
</html>
```